Harborline Quoting
Business Cards and Stationery for Service Co
Simple
Dane Corwell
Vice President
20436 SW 47th Avenue Suite 3105 Vancouver, WA 97531
danec@harborlinequoting.com
www.harborlinequoting.com
Please keep it simple and professional.
Just the logo

```html
<!DOCTYPE html>
<html lang="en">
<head>
<meta charset="utf-8">
<title>Harborline Quoting — Business Cards</title>
<link rel="stylesheet" href="https://fonts.googleapis.com/css2?family=Open+Sans:wght@400;600;700&display=swap">
<style>
  :root {
    --brand-orange: #d9532a;
    --ink: #4a4a4a;
    --ink-soft: #6b6b6b;
    --card: #ffffff;
    --backdrop: #e4e4e2;
  }
  * { margin: 0; padding: 0; box-sizing: border-box; }
  html, body { width: 1200px; height: 804px; overflow: hidden; }
  body {
    background: var(--backdrop);
    font-family: "Open Sans", Arial, sans-serif;
    color: var(--ink);
  }
  .sheet {
    position: relative;
    width: 1200px;
    height: 804px;
  }
  .card {
    position: absolute;
    top: 253px;
    width: 520px;
    height: 298px;
    background: var(--card);
    box-shadow: 0 6px 18px rgba(0,0,0,0.12);
  }
  .card--front { left: 60px; }
  .card--back { left: 620px; }

  /* Front */
  .brand {
    position: absolute;
    top: 44px;
    left: 34px;
    display: flex;
    align-items: center;
    gap: 10px;
  }
  .brand__dot {
    width: 38px;
    height: 38px;
    border-radius: 50%;
    background: var(--brand-orange);
  }
  .brand__name {
    font-weight: 700;
    font-size: 19px;
    letter-spacing: 1.5px;
    text-transform: uppercase;
    color: var(--brand-orange);
    line-height: 1;
  }
  .contact {
    position: absolute;
    top: 44px;
    right: 32px;
    text-align: right;
    font-size: 10.5px;
    line-height: 15px;
    color: var(--ink-soft);
  }
  .contact__gap { height: 6px; }
  .person {
    position: absolute;
    left: 34px;
    top: 176px;
  }
  .person__name {
    font-size: 19px;
    font-weight: 400;
    color: var(--ink);
    line-height: 1.1;
  }
  .person__title {
    font-size: 11px;
    font-weight: 600;
    color: var(--brand-orange);
    margin-top: 3px;
  }
  .person__address {
    font-size: 10.5px;
    line-height: 14px;
    color: var(--ink-soft);
    margin-top: 6px;
  }
  .accent-line {
    position: absolute;
    left: 150px;
    right: 0;
    top: 226px;
    height: 3px;
    background: linear-gradient(to right, rgba(217,83,42,0), var(--brand-orange) 45%, var(--brand-orange));
  }

  /* Back */
  .back-mark {
    position: absolute;
    inset: 0;
    display: flex;
    flex-direction: column;
    align-items: center;
    justify-content: center;
    gap: 14px;
  }
  .back-mark__circle {
    width: 130px;
    height: 130px;
    border-radius: 50%;
    background: var(--brand-orange);
  }
  .back-mark__name {
    font-weight: 700;
    font-size: 16px;
    letter-spacing: 1.5px;
    text-transform: uppercase;
    color: var(--brand-orange);
  }
</style>
</head>
<body>
<main class="sheet">
  <section class="card card--front" aria-label="Business card front">
    <div class="brand">
      <span class="brand__dot" aria-hidden="true"></span>
      <span class="brand__name">Harborline Quoting</span>
    </div>

    <div class="contact">
      <p>Tel: 360-555-0148</p>
      <p>Fax: 888-555-0173</p>
      <div class="contact__gap"></div>
      <p>Email: danec@harborlinequoting.com</p>
      <p>www.harborlinequoting.com</p>
    </div>

    <div class="accent-line" aria-hidden="true"></div>

    <div class="person">
      <p class="person__name">Dane Corwell</p>
      <p class="person__title">Vice President</p>
      <p class="person__address">20436 SW 47th Avenue<br>Suite 3105</p>
    </div>
  </section>

  <section class="card card--back" aria-label="Business card back">
    <div class="back-mark">
      <span class="back-mark__circle" aria-hidden="true"></span>
      <span class="back-mark__name">Harborline Quoting</span>
    </div>
  </section>
</main>
</body>
</html>
```